Business Card for a Life Coaching Company

BRAVOPEAK is a Life Coaching company that was initiated to support people who want to transform thier life or ana aspect of it.
our slogan is : "Dream. Believe. Succeed"
our logo is uploaded.
The name of the company implies that leadership, strength and wisdom required to change your life.
We want an attractive business card that would give an impression of reliability, support and change. so we really want it unique. Here are some examples of unique cards:

http://www.cardcraftvault.example/2009/05/100-really-creative-business-cards/

BravoPeak is a life coaching organization focusing on individual transformation through the application of relevant and timeless principles of success.  BravoPeak believes that real, sustainable life transformations are brought about by tuning into the timeless wisdom we each carry in our hearts while boldy acting in the direction of our dreams.

Contacts on the card:
Address: 7 Tarek Nour El Dine Heliopolis Cairo Egypt
Tel: +202 24 71 38 52
Fax: +202 24 71 38 17
Mobile: +2 012 684 2097 (Dalia Soliman)
+2 0199915815 (Tariq Bhatti)

By the way, our temporary website is http://www.bravopeak.example

We have attached an .eps file with various configurations of our logo.

```html
<!DOCTYPE html>
<html lang="en">
<head>
<meta charset="utf-8">
<title>BRAVOPEAK Business Card</title>
<link rel="stylesheet" href="https://fonts.googleapis.com/css2?family=Cinzel:wght@400&family=Tinos&family=Arimo&display=swap">
<style>
  :root {
    --brand-red: #f04a22;
    --slogan-red: #f07563;
    --ink: #3a3a3a;
    --label-ink: #111111;
    --paper: #ffffff;
    --frame: #222222;
  }
  html, body {
    margin: 0;
    padding: 0;
    overflow: hidden;
    background: var(--paper);
  }
  .sheet {
    position: relative;
    width: 1200px;
    height: 1025px;
    overflow: hidden;
    background: var(--paper);
  }
  .sheet-label {
    position: absolute;
    left: 8px;
    margin: 0;
    font-family: "Arimo", Arial, sans-serif;
    font-size: 22px;
    font-weight: 400;
    color: var(--label-ink);
  }
  .sheet-label--front { top: 10px; }
  .sheet-label--back { top: 530px; }

  .card {
    position: absolute;
    left: 8px;
    width: 695px;
    height: 414px;
    box-sizing: border-box;
  }
  .card--front {
    top: 50px;
    background: var(--brand-red);
    border: 2px solid var(--frame);
  }
  .card--back {
    top: 588px;
    background: var(--paper);
    border: 2px solid var(--frame);
  }

  .front-mark {
    position: absolute;
    left: 42px;
    top: 107px;
    width: 190px;
    height: 190px;
  }
  .front-name {
    position: absolute;
    left: 258px;
    top: 60px;
    margin: 0;
    font-family: "Cinzel", "Trajan Pro", serif;
    font-weight: 400;
    font-size: 112px;
    line-height: 148px;
    letter-spacing: 2px;
    color: var(--paper);
  }
  .front-name span { display: block; }

  .slogan {
    position: absolute;
    right: 26px;
    top: 22px;
    margin: 0;
    text-align: right;
    font-family: "Cinzel", "Trajan Pro", serif;
    font-weight: 400;
    font-size: 62px;
    line-height: 66px;
    letter-spacing: -1px;
    color: var(--slogan-red);
  }
  .slogan span { display: block; }

  .contact {
    position: absolute;
    left: 30px;
    bottom: 20px;
    margin: 0;
    font-family: "Tinos", "Times New Roman", serif;
    font-style: normal;
    font-size: 21px;
    line-height: 31px;
    color: var(--ink);
  }
  .contact span { display: block; }

  .logo-lockup {
    position: absolute;
    left: 790px;
    top: 870px;
    width: 405px;
    height: 130px;
  }
  .logo-lockup__mark {
    position: absolute;
    left: 162px;
    top: 0;
    width: 72px;
    height: 72px;
  }
  .logo-lockup__name {
    position: absolute;
    left: 0;
    right: 0;
    top: 70px;
    margin: 0;
    text-align: center;
    font-family: "Cinzel", "Trajan Pro", serif;
    font-weight: 400;
    font-size: 46px;
    line-height: 56px;
    color: var(--ink);
  }
</style>
</head>
<body>
<main class="sheet">
  <h2 class="sheet-label sheet-label--front">Business Card front</h2>
  <section class="card card--front" aria-label="Business card front">
    <svg class="front-mark" viewBox="0 0 190 190" aria-hidden="true">
      <circle cx="95" cy="95" r="92" fill="var(--paper)"/>
    </svg>
    <h1 class="front-name"><span>BRAVO</span><span>PEAK</span></h1>
  </section>

  <h2 class="sheet-label sheet-label--back">Business Card back</h2>
  <section class="card card--back" aria-label="Business card back">
    <p class="slogan"><span>Dream.</span><span>Believe.</span><span>Succeed.</span></p>
    <address class="contact">
      <span>7 Tarek Nour El Dine Heliopolis Cairo Egypt</span>
      <span>Tel: +202 24 71 38 52 Fax: +202 24 71 38 17</span>
      <span>Mobile: +2 012 684 2097 (Dalia Soliman)</span>
      <span>+2 0197328406 (Tariq Bhatti)</span>
    </address>
  </section>

  <div class="logo-lockup" aria-label="BRAVOPEAK logo">
    <svg class="logo-lockup__mark" viewBox="0 0 72 72" aria-hidden="true">
      <circle cx="36" cy="36" r="34" fill="var(--brand-red)"/>
    </svg>
    <p class="logo-lockup__name">BRAVOPEAK</p>
  </div>
</main>
</body>
</html>
```